App for Lawyers & Accountants needs 'Professional' Styling

We want to style our app to convey a 'Professional' appearance. It's used by Lawyers, Accountants, Doctors etc. who take their work very seriously.

We currently trying to follow corvane layout guidelines, but we find our app looks very bland. I've uploaded a screenshot of our current app, and two mock-ups of more stylized versions, but we're not happy with those mock-ups.

We'd like to see alternate designs for those two mock-ups, that look much more professional.

The specific elements we'd like to improve/focus on are:
* Colour of the top and left nav bars
* Appearance of the left nav, size, icons spacing
* Appearance of the buttons on the top right, so the user knows they are buttons they can press
* Spacing of the dashboard, background colour and spacing, colour/layout of the 'overdue' and 'todo' accordion headings in the 'my tasks' section.
* List view background grey, to be consistent with dashboard, but unobtrusive
* List view tabs to be obvious as tabs, but 'saved searches', filters and the export icon to still be associated with the data displayed, but it should be obvious to the user that those are different buttons, not just more tabs. (I.e. the filters button opens a panel below it that allows the user to filter the data in the list.)
* General appearance of the popup menu when you push the 'add' button on the top right

However, despite those specifics I'm sure it's all the subtle elements of the design that make a big difference.

Our brand colour is 1D4F91, and we use A20067 as a secondary colour in print media, (although it doesn't seem to work to well within the app.) Our brand font is signika. We'd like the designs to be based on those colours & font.

Professional people, Lawyers, Accountants, Doctors etc.

Sans Serif
• Signika

0255a3

• The most 'Professional' experience/quality possible. Think the quality & brand image of brindlewave desk, but taken to a higher level.
• An example/mock-up of the dashboard, list view and 'add' item popup menu
• Display the dashboard cards with the same information as our mock-ups - the information there is important and we don't have any extra cards to add (in the near term)
• Various colour combinations for the top and left nav bars, based on our primary blue brand colour, and perhaps some shade of dark grey.

```html
<!DOCTYPE html>
<html lang="en">
<head>
<meta charset="utf-8">
<title>Matters</title>
<link href="https://fonts.googleapis.com/css2?family=Signika:wght@300;400;500;600&display=swap" rel="stylesheet">
<style>
  :root {
    --page-bg: #f6f7f9;
    --page-shape: #eceef2;
    --brand-blue: #0255a3;
    --accent: #ffc20e;
    --white: #ffffff;
    --ink: #1b1b1b;
    --text-strong: #4a4d52;
    --text-muted: #9a9da3;
    --rule: #d6d8dc;
    --icon-muted: #b8bbc0;
    --chip-bg: #ececec;
  }
  * { box-sizing: border-box; margin: 0; padding: 0; }
  html, body { width: 1200px; height: 1000px; overflow: hidden; }
  body { background: var(--page-bg); font-family: 'Signika', sans-serif; position: relative; }
  .backdrop { position: absolute; inset: 0; }

  .app-window {
    position: absolute; left: 38px; top: 184px; width: 1124px; height: 631px;
    background: var(--white); border-radius: 16px; overflow: hidden;
    box-shadow: 0 12px 40px rgba(40, 50, 70, 0.12);
  }

  .side-nav { position: absolute; left: 0; top: 0; width: 58px; height: 100%; background: var(--white); }
  .brand { position: absolute; left: 0; top: 12px; width: 58px; text-align: center; }
  .brand-dot { display: block; width: 10px; height: 10px; border-radius: 50%; background: var(--ink); margin: 0 auto 3px; }
  .brand-name { font-size: 10px; font-weight: 600; color: var(--ink); }
  .nav-icon { position: absolute; left: 18px; width: 22px; height: 22px; }
  .nav-active-bar { position: absolute; left: 56px; top: 246px; width: 2px; height: 36px; background: var(--accent); }

  .top-bar { position: absolute; left: 58px; top: 0; right: 0; height: 190px; background: var(--brand-blue); color: var(--white); }
  .search { position: absolute; left: 56px; top: 22px; width: 328px; height: 22px; border-bottom: 1.5px solid var(--white); font-size: 10px; font-weight: 500; }
  .search svg { position: absolute; right: 0; top: 1px; }
  .quick-btn { position: absolute; top: 22px; width: 23px; height: 23px; border-radius: 50%; background: var(--accent); display: flex; align-items: center; justify-content: center; }
  .avatar { position: absolute; left: 921px; top: 22px; width: 23px; height: 23px; border-radius: 50%; background: linear-gradient(135deg, #e9d6cf, #7b5448); border: 2px solid var(--white); }
  .avatar-caret { position: absolute; left: 927px; top: 48px; }
  .add-btn { position: absolute; left: 962px; top: 10px; width: 48px; height: 48px; border-radius: 50%; background: var(--accent); display: flex; align-items: center; justify-content: center; }
  .page-title { position: absolute; left: 56px; top: 84px; font-size: 26px; font-weight: 400; }
  .tabs { position: absolute; left: 56px; top: 146px; display: flex; list-style: none; }
  .tab { width: 117px; height: 44px; text-align: center; font-size: 10.5px; font-weight: 500; padding-top: 9px; }
  .tab.is-active { color: var(--accent); border-bottom: 3px solid var(--accent); }
  .filter-btn { position: absolute; left: 905px; top: 146px; width: 105px; height: 32px; border: 1px solid var(--white); border-radius: 16px; font-size: 10.5px; font-weight: 500; display: flex; align-items: center; justify-content: center; gap: 18px; }

  .matters-table { position: absolute; left: 114px; top: 216px; width: 954px; border-collapse: collapse; }
  .matters-table th { font-size: 13.5px; font-weight: 400; color: var(--text-muted); text-align: left; height: 44px; border-bottom: 1px solid var(--rule); letter-spacing: 0.2px; }
  .matters-table td { font-size: 11px; color: var(--text-muted); height: 48.7px; }
  .matters-table td.title { color: var(--text-strong); }
  .checkbox { display: inline-block; width: 9px; height: 9px; border: 1px solid #c8cacd; vertical-align: middle; }
  .col-check { width: 48px; }
  .col-check svg { vertical-align: middle; margin-left: 8px; }
  .col-title { width: 373px; }
  .col-client { width: 146px; }
  .col-area { width: 129px; }
  .col-stage { width: 128px; }

  .pagination { position: absolute; left: 534px; top: 541px; display: flex; align-items: center; gap: 12px; font-size: 12px; color: var(--text-muted); }
  .per-page { position: absolute; left: 978px; top: 540px; display: flex; align-items: center; gap: 12px; font-size: 12px; color: var(--text-muted); }
  .per-page-count { background: var(--chip-bg); color: var(--ink); width: 26px; height: 20px; display: flex; align-items: center; justify-content: center; }
</style>
</head>
<body>
  <svg class="backdrop" width="1200" height="1000" aria-hidden="true">
    <polygon points="0,20 478,150 520,260 0,260" fill="#eef0f3"/>
    <polygon points="0,860 560,1000 900,1000 805,815 0,815" fill="#eceef2"/>
  </svg>

  <main class="app-window">
    <nav class="side-nav">
      <div class="brand"><span class="brand-dot"></span><span class="brand-name">Tarno</span></div>
      <svg class="nav-icon" style="top:214px" viewBox="0 0 22 22" fill="none" stroke="#b8bbc0" stroke-width="1.2"><path d="M3 8 L11 3 L19 8 Z"/><path d="M5 9v8M9 9v8M13 9v8M17 9v8M3 18h16"/></svg>
      <svg class="nav-icon" style="top:250px" viewBox="0 0 22 22" fill="none" stroke="#ffc20e" stroke-width="1.5"><rect x="3" y="7" width="16" height="11" rx="1.5"/><path d="M8 7V5h6v2M3 11h16"/></svg>
      <div class="nav-active-bar"></div>
      <svg class="nav-icon" style="top:286px" viewBox="0 0 22 22" fill="none" stroke="#b8bbc0" stroke-width="1.2"><circle cx="11" cy="7" r="4"/><path d="M4 19c0-4 3-6 7-6s7 2 7 6z"/></svg>
      <svg class="nav-icon" style="top:324px" viewBox="0 0 22 22" fill="none" stroke="#b8bbc0" stroke-width="1.2"><rect x="4" y="4" width="14" height="16" rx="1"/><path d="M8 3h6v3H8zM8 12l2.5 2.5L15 10"/></svg>
      <svg class="nav-icon" style="top:361px" viewBox="0 0 22 22" fill="none" stroke="#b8bbc0" stroke-width="1.2"><path d="M15 7l-7 7a2 2 0 0 0 3 3l8-8a4 4 0 0 0-6-6l-8 8a6 6 0 0 0 8 8l6-6"/></svg>
      <svg class="nav-icon" style="top:397px" viewBox="0 0 22 22" fill="none" stroke="#b8bbc0" stroke-width="1.2"><circle cx="11" cy="12" r="7"/><path d="M11 8v4l3 2M3 5l3-2M19 5l-3-2"/></svg>
      <svg class="nav-icon" style="top:569px" viewBox="0 0 22 22" fill="none" stroke="#1b1b1b" stroke-width="1.3"><polygon points="11,2 18.8,6.5 18.8,15.5 11,20 3.2,15.5 3.2,6.5"/><circle cx="11" cy="11" r="3.5"/></svg>
      <svg class="nav-icon" style="top:603px" viewBox="0 0 22 22" fill="none" stroke="#1b1b1b" stroke-width="1.5"><path d="M18 11H4M10 5l-6 6 6 6"/></svg>
    </nav>

    <header class="top-bar">
      <div class="search">Search
        <svg width="11" height="11" viewBox="0 0 11 11" fill="none" stroke="#fff" stroke-width="1.5"><circle cx="4.5" cy="4.5" r="3.5"/><path d="M7 7l3 3"/></svg>
      </div>
      <div class="quick-btn" style="left:837px">
        <svg width="13" height="13" viewBox="0 0 13 13" fill="none" stroke="#0255a3" stroke-width="1.4"><circle cx="6.5" cy="6.5" r="5"/><path d="M6.5 3.5v3l2 1.5"/></svg>
      </div>
      <div class="quick-btn" style="left:879px">
        <svg width="12" height="12" viewBox="0 0 12 12" fill="#0255a3"><path d="M6 1a3.5 3.5 0 0 0-3.5 3.5V8L1.5 9.5h9L9.5 8V4.5A3.5 3.5 0 0 0 6 1z"/><circle cx="6" cy="10.8" r="1.1"/></svg>
      </div>
      <div class="avatar" role="img" aria-label="User profile photo"></div>
      <svg class="avatar-caret" width="8" height="5" viewBox="0 0 8 5" fill="none" stroke="#fff" stroke-width="1.3"><path d="M1 1l3 3 3-3"/></svg>
      <div class="add-btn">
        <svg width="20" height="20" viewBox="0 0 20 20" stroke="#fff" stroke-width="2.2"><path d="M10 2v16M2 10h16"/></svg>
      </div>
      <h1 class="page-title">Matters</h1>
      <ul class="tabs">
        <li class="tab is-active">My Matter</li>
        <li class="tab">Recent Matters</li>
        <li class="tab">All Matters</li>
        <li class="tab">Saved Search</li>
      </ul>
      <div class="filter-btn">Filter
        <svg width="12" height="9" viewBox="0 0 12 9" stroke="#fff" stroke-width="1.3"><path d="M0 1h12M2 4.5h8M4 8h4"/></svg>
      </div>
    </header>

    <table class="matters-table">
      <thead>
        <tr>
          <th class="col-check"><span class="checkbox"></span></th>
          <th class="col-title">Title</th>
          <th class="col-client">Client</th>
          <th class="col-area">Practice Area</th>
          <th class="col-stage">Stage</th>
          <th>Last Updated</th>
        </tr>
      </thead>
      <tbody>
        <tr>
          <td class="col-check"><span class="checkbox"></span><svg width="12" height="12" viewBox="0 0 12 12"><polygon points="6,0.5 7.6,4.2 11.6,4.5 8.6,7.1 9.5,11 6,8.9 2.5,11 3.4,7.1 0.4,4.5 4.4,4.2" fill="#ffc20e"/></svg></td>
          <td class="title">Abbott v. Moore concering sale #707</td>
          <td>M Harrow</td><td>Conveyancing</td><td>Sign up</td><td>30/06/2017</td>
        </tr>
        <tr>
          <td class="col-check"><span class="checkbox"></span><svg width="12" height="12" viewBox="0 0 12 12"><polygon points="6,0.5 7.6,4.2 11.6,4.5 8.6,7.1 9.5,11 6,8.9 2.5,11 3.4,7.1 0.4,4.5 4.4,4.2" fill="none" stroke="#9a9da3"/></svg></td>
          <td class="title">Abernathy v. Director of Public Prosecutions con deceases #310</td>
          <td>Nicolas Inc</td><td>Estates</td><td>Complete</td><td>16/04/2017</td>
        </tr>
        <tr>
          <td class="col-check"><span class="checkbox"></span><svg width="12" height="12" viewBox="0 0 12 12"><polygon points="6,0.5 7.6,4.2 11.6,4.5 8.6,7.1 9.5,11 6,8.9 2.5,11 3.4,7.1 0.4,4.5 4.4,4.2" fill="#ffc20e"/></svg></td>
          <td class="title">Abernathy v. Director of Public Prosecutions con investment #578</td>
          <td>Little and Rogan</td><td>Property</td><td>Settlement</td><td>05/03/2017</td>
        </tr>
        <tr>
          <td class="col-check"><span class="checkbox"></span><svg width="12" height="12" viewBox="0 0 12 12"><polygon points="6,0.5 7.6,4.2 11.6,4.5 8.6,7.1 9.5,11 6,8.9 2.5,11 3.4,7.1 0.4,4.5 4.4,4.2" fill="#ffc20e"/></svg></td>
          <td class="title">Abernathy v. Director of Public Prosecutions con work cover #295</td>
          <td>D'Amore Zieman</td><td>Personal Injury</td><td>Sign up</td><td>02/09/2017</td>
        </tr>
        <tr>
          <td class="col-check"><span class="checkbox"></span><svg width="12" height="12" viewBox="0 0 12 12"><polygon points="6,0.5 7.6,4.2 11.6,4.5 8.6,7.1 9.5,11 6,8.9 2.5,11 3.4,7.1 0.4,4.5 4.4,4.2" fill="none" stroke="#9a9da3"/></svg></td>
          <td class="title">Abernathy v. Schmitt concerning retail lease #668</td>
          <td>Writting and Leucscke</td><td>Property</td><td>Settlement</td><td>15/11/2017</td>
        </tr>
      </tbody>
    </table>

    <div class="pagination">
      <svg width="8" height="11" viewBox="0 0 8 11" fill="none" stroke="#9a9da3" stroke-width="1.5"><path d="M6 1L2 5.5 6 10"/></svg>
      <span>1 - 5 of 157</span>
      <svg width="8" height="11" viewBox="0 0 8 11" fill="none" stroke="#1b1b1b" stroke-width="1.5"><path d="M2 1l4 4.5L2 10"/></svg>
    </div>
    <div class="per-page"><span class="per-page-count">20</span><span>per page</span></div>
  </main>
</body>
</html>
```